Membership Welcome Package

Thank you I have selected a designer and am closing this competition early.
Kind regards,
Nola
Updates

sample of corporate branding use (for inspiration) re-uploaded on document "KLMO Membership".

I hope it helps.
Nola :)

Hello Designer and thank your or you submissions.

I am under pressure to have this document ready, so am closing the competition early.
Please do not submit any further new designs.
Thank you very much for being part of this competition.
Nola :)

Target Market(s)

business owners and managers in a regional "downtown" or "highstreet" shopping district.

Requirements
Must have
• Editable by me via Word! Sorry I do not have any publisher programs!

Must be in colour guidelines as per corporate identity document
Nice to have
• I am open to design, but I think that it should communicate warmth, community and caring - as well as being business-oriented.
I have plenty more logo files if required!

```html
<!DOCTYPE html>
<html lang="en">
<head>
<meta charset="utf-8">
<title>KLMO New Members Welcome Package</title>
<link rel="stylesheet" href="https://fonts.googleapis.com/css2?family=Poppins:wght@800&family=Arimo:wght@400;700&display=swap">
<style>
  :root {
    --backdrop: #d9d9d6;
    --paper: #ffffff;
    --ink: #111111;
    --body-ink: #222222;
    --cyan: #1ba6d3;
    --yellow: #fcc419;
    --photo-sky: #c9d3da;
    --photo-street: #8d8176;
    --campaign-tone: #2b2b2b;
  }
  * { box-sizing: border-box; margin: 0; padding: 0; }
  html, body { width: 1200px; height: 849px; overflow: hidden; }
  body { background: var(--backdrop); position: relative; font-family: "Arimo", Arial, sans-serif; }

  .page {
    position: absolute; left: 300px; top: 0;
    width: 600px; height: 849px;
    background: var(--paper);
    overflow: hidden;
  }

  .street-photo {
    position: absolute; left: 0; top: 0; width: 600px; height: 92px;
    background: linear-gradient(180deg, var(--photo-sky) 0%, #b8b3a8 55%, var(--photo-street) 100%);
  }
  .corner-banner { position: absolute; left: 0; top: 0; }
  .corner-name {
    position: absolute; left: 432px; top: 62px;
    font-family: "Arimo", Arial, sans-serif; font-weight: 700; font-size: 25px; line-height: 25px;
    color: var(--paper); transform: rotate(-29deg); transform-origin: left center;
  }

  .title {
    position: absolute; left: 34px; top: 116px;
    font-family: "Poppins", sans-serif; font-weight: 800;
    font-size: 33px; line-height: 34px; color: var(--ink); letter-spacing: 0.2px;
  }

  .content { position: absolute; left: 34px; top: 204px; width: 528px; color: var(--body-ink); }
  .section-heading {
    font-family: "Arimo", Arial, sans-serif; font-weight: 700;
    font-size: 16px; color: var(--cyan); margin-bottom: 13px;
  }
  .content p { font-size: 9.4px; line-height: 12px; text-align: justify; }
  .sub-heading { font-weight: 700; margin-top: 14px; }
  .content p.sub-heading { font-size: 10px; }
  .section + .section { margin-top: 34px; }
  .benefits { list-style: none; font-size: 9.4px; line-height: 12px; }
  .benefits li { padding-left: 14px; position: relative; }
  .benefits li::before { content: "•"; position: absolute; left: 2px; }

  .accent-corner { position: absolute; left: 0; top: 622px; }

  .campaign-line {
    position: absolute; left: 308px; top: 784px; width: 158px; height: 54px;
    background: var(--campaign-tone);
  }
  .footer-rule { position: absolute; left: 487px; top: 766px; width: 1px; height: 72px; background: var(--ink); }
  .footer-bar { position: absolute; left: 308px; top: 841px; width: 278px; height: 8px; background: var(--ink); }
  .association-mark {
    position: absolute; left: 496px; top: 782px; width: 100px;
    display: flex; align-items: center; gap: 6px;
  }
  .association-mark .dot { flex: none; width: 18px; height: 18px; border-radius: 50%; background: var(--ink); }
  .association-mark .name {
    font-family: "Arimo", Arial, sans-serif; font-weight: 700; font-size: 8.5px;
    line-height: 10px; color: var(--ink);
  }
</style>
</head>
<body>
  <main class="page">
    <div class="street-photo" role="img" aria-label="Photograph of a town main street with shopfronts and a road"></div>
    <svg class="corner-banner" width="600" height="92" viewBox="0 0 600 92" aria-hidden="true">
      <polygon points="372,0 600,0 600,8 448,92 425,92" fill="var(--yellow)"/>
    </svg>
    <span class="corner-name">kelmore</span>

    <h1 class="title">New Members<br>Welcome Package</h1>

    <div class="content">
      <section class="section">
        <h2 class="section-heading">Relationship Building</h2>
        <p>Get to know clients, colleagues, suppliers and competitors in a relaxed, friendly networking environment. Each month at least one networking event will be held to provide a forum for members to build and grow relationships with existing and potential clients, colleagues, competitors, suppliers and local government representatives.<br>
        The Kelmore Town Business Association creates a social and open environment for businesses to interact, with a focus on a culture of giving and assisting others.<br>
        New members have the opportunity to network and seek out advice from the many professionals and other business colleagues who are members of the Association.</p>

        <p class="sub-heading">Monthly Networking:</p>
        <p>Each month, Kelmore Town Business Association hosts a Business Breakfast Networking Function, providing local businesses with invaluable business contacts. Save this time in your business diary, and bring along your business cards, and network with local and regional businesses. Each month there is a special guest speaker and an opportunity for a member to profile their business. Kelmore Business Breakfasts are held on the last Wednesday of the month at 7.15am for 7.30 start – 8.30am – venue to be advised.</p>

        <p class="sub-heading">Quarterly Networking:</p>
        <p>Business and Community Network Meetings are held in partnership with the Service Club of Kelmore /Ashvale and the Kelmore Town Business Association. These meetings are held in the evening and hosted by local businesses. If you would like to host a network meeting contact Jan Corbett on 0400 123 456.</p>
      </section>

      <section class="section">
        <h2 class="section-heading">Business Development</h2>
        <p>Develop your skill and your business. If you have a business development need, we probably have information of know someone who can help you.<br>
        The Association proposes to establish regular networking sessions, to teach members the theory and strategy of effective networking, whilst providing a wide range of business development workshops and functions with an educational focus.<br>
        Advice on Human Resources, Workplace Safety, International Trade, Industrial Relations and free access to an Industrial Relations Workplace advice hotline is available through the Association's alliance partners.<br>
        The Kelmore Town Business Association offers access to assistance with government funded traineeships and apprenticeships.</p>
        <ul class="benefits">
          <li>Association Events, Speed Networking, Networking Events</li>
          <li>Online Promotion, Category Listing (Retail, Home Service, Entertainment)</li>
          <li>Education Programs</li>
          <li>Awards, For Excellence and recognition</li>
        </ul>
      </section>
    </div>

    <svg class="accent-corner" width="110" height="227" viewBox="0 0 110 227" role="img" aria-label="Cyan corner band carrying a short campaign word">
      <polygon points="0,0 104,227 0,227" fill="var(--cyan)"/>
    </svg>

    <div class="campaign-line" role="img" aria-label="Campaign slogan lettering"></div>
    <div class="footer-rule"></div>
    <div class="association-mark">
      <span class="dot"></span>
      <span class="name">Kelmore<br>Town Business<br>Association</span>
    </div>
    <div class="footer-bar"></div>
  </main>
</body>
</html>
```